Lumo Sourdough Tortilla bag design front and back

Our tortilla bags are flat plastic bags. I would like a design for the front and back of our tortillas. Our tortillas are made of whole wheat flour. We have decided to go with the following font and color scheme for our tortilla bags from the updated attached samples below. Wheat or taco images are okay to brighten and make the package stand out. We prefer a clean look. We prefer the word "Artisian" to remain in cursive.

Target Market(s)

Health conscious consumers

Industry/Entity Type

Bakery

Font styles to use
Serif
Sans Serif
Decorative

Colors
59FF00
82FF00
B8FF75
E3FFCB
F4FFEA
EB3D1F
EC4F4E
F09395
F8D3D4
FCEDEE

Requirements
Must have
• The word "sourdough must standout and be prominent on the front,
Nice to have
• Looking for clean upscale look that pops

```html
<!DOCTYPE html>
<html lang="en">
<head>
<meta charset="utf-8">
<title>Lumo Sourdough Tortilla – Bag Front</title>
<link rel="stylesheet" href="https://fonts.googleapis.com/css2?family=Anton&family=Kaushan+Script&family=Montserrat:wght@700;800;900&family=Oswald:wght@400;500;700&family=Yellowtail&display=block">
<style>
  :root {
    --leaf: #a2d13f;
    --forest: #2b3a1f;
    --night: #0c0d10;
    --paper: #ffffff;
  }
  * { box-sizing: border-box; margin: 0; padding: 0; }
  html, body { width: 1200px; height: 1200px; overflow: hidden; background: var(--paper); }
  .bag-front { position: relative; width: 1200px; height: 1200px; overflow: hidden; }

  .band { position: absolute; left: 0; width: 1200px; }
  .band--top { top: 0; height: 207px; background: var(--leaf); }
  .band--window { top: 207px; height: 327px; background: var(--paper); }
  .band--title { top: 534px; height: 332px; background: var(--night); }
  .band--base { top: 866px; height: 334px; background: var(--leaf); }

  .brand-name {
    position: absolute; top: 44px; left: 0; width: 1200px; text-align: center;
    font-family: "Montserrat", sans-serif; font-weight: 900; font-size: 72px; line-height: 1;
    letter-spacing: 1px; color: var(--forest);
  }

  .product-title {
    position: absolute; top: 588px; left: 0; width: 1200px; text-align: center;
    font-family: "Anton", sans-serif; font-weight: 400; font-size: 166px; line-height: 1;
    letter-spacing: 3px; color: var(--leaf);
    transform: scaleX(0.8); transform-origin: 598px 0;
  }
  .title-rule { position: absolute; top: 795px; height: 3px; background: var(--leaf); }
  .title-rule--left { left: 290px; width: 247px; }
  .title-rule--right { left: 672px; width: 243px; }
  .title-emblem {
    position: absolute; left: 562px; top: 770px; width: 82px; height: 50px;
    border-radius: 50% 50% 40% 40%; background: rgba(255,255,255,0.85);
  }

  .product-type__script {
    position: absolute; left: 300px; top: 912px; width: 610px; text-align: center;
    font-family: "Kaushan Script", "Yellowtail", cursive; font-size: 82px; line-height: 1.1;
    color: var(--paper); transform: rotate(-4deg);
  }
  .product-type__name {
    position: absolute; left: 300px; top: 986px; width: 610px; text-align: center;
    font-family: "Montserrat", sans-serif; font-weight: 900; font-size: 102px; line-height: 1;
    letter-spacing: 2px; color: var(--forest);
    transform: scaleX(0.82); transform-origin: 305px 0;
  }

  .badge-label {
    position: absolute; font-family: "Montserrat", sans-serif; font-weight: 800;
    font-size: 12.5px; color: var(--forest); text-align: center;
  }
  .badge-vegan {
    position: absolute; left: 73px; top: 925px; width: 170px; height: 78px;
    border-radius: 12px; background: var(--forest);
  }
  .icon { position: absolute; }

  .count-box {
    position: absolute; left: 985px; top: 1040px; width: 117px; height: 64px;
    background: var(--forest); color: var(--paper); display: flex; align-items: center; justify-content: center;
    font-family: "Oswald", sans-serif; line-height: 1;
  }
  .count-box__num { font-weight: 700; font-size: 56px; }
  .count-box__unit { font-weight: 500; font-size: 44px; margin-top: 4px; }
  .net-weight {
    position: absolute; left: 985px; top: 1118px; font-family: "Oswald", sans-serif;
    font-size: 24px; line-height: 1.08; color: var(--paper); letter-spacing: 0.5px;
  }
  .net-weight__rule { display: inline-block; width: 56px; height: 2px; background: var(--paper); vertical-align: 2px; }

  .storage-note {
    position: absolute; left: 524px; top: 1138px; height: 32px; padding: 0 8px;
    border: 1.5px solid var(--night); border-radius: 3px;
    font-family: "Oswald", sans-serif; font-size: 22px; line-height: 29px; color: var(--night);
  }
  .storage-note__flake { position: absolute; left: 654px; top: 1130px; }
</style>
</head>
<body>
<main class="bag-front">
  <div class="band band--top"></div>
  <div class="band band--window"></div>
  <div class="band band--title"></div>
  <div class="band band--base"></div>

  <h1 class="brand-name">LUMO</h1>

  <h2 class="product-title">SOURDOUGH</h2>
  <div class="title-rule title-rule--left"></div>
  <div class="title-emblem" role="img" aria-label="Small white lotus emblem"></div>
  <div class="title-rule title-rule--right"></div>

  <span class="product-type__script">Artisan</span>
  <span class="product-type__name">TORTILLAS</span>

  <div class="badge-vegan" role="img" aria-label="Vegan badge"></div>

  <svg class="icon" style="left:73px;top:1040px" width="72" height="72" viewBox="0 0 72 72" aria-hidden="true">
    <circle cx="36" cy="36" r="33" fill="none" stroke="var(--forest)" stroke-width="5"/>
    <line x1="13" y1="13" x2="59" y2="59" stroke="var(--forest)" stroke-width="5"/>
  </svg>
  <div class="badge-label" style="left:73px;top:1118px;width:72px">NO SOY</div>

  <svg class="icon" style="left:170px;top:1040px" width="72" height="72" viewBox="0 0 72 72" aria-hidden="true">
    <circle cx="36" cy="36" r="33" fill="none" stroke="var(--forest)" stroke-width="5"/>
    <line x1="13" y1="13" x2="59" y2="59" stroke="var(--forest)" stroke-width="5"/>
  </svg>
  <div class="badge-label" style="left:160px;top:1118px;width:92px">NON GMO</div>

  <svg class="icon" style="left:1020px;top:890px" width="94" height="94" viewBox="0 0 94 94" aria-hidden="true">
    <circle cx="47" cy="47" r="43" fill="none" stroke="var(--paper)" stroke-width="6"/>
    <line x1="17" y1="17" x2="77" y2="77" stroke="var(--paper)" stroke-width="6"/>
  </svg>
  <div class="badge-label" style="left:990px;top:996px;width:154px;color:var(--paper);font-size:13.5px">NO ADDED SALT</div>

  <div class="count-box"><span class="count-box__num">8</span><span class="count-box__unit">CT</span></div>
  <div class="net-weight">NET WEIGHT<span class="net-weight__rule"></span><br>12 OUNCES / 243 G</div>

  <div class="storage-note">KEEP FROZEN</div>
  <svg class="storage-note__flake" width="28" height="28" viewBox="0 0 28 28" aria-hidden="true">
    <g stroke="var(--night)" stroke-width="3" stroke-linecap="round">
      <line x1="14" y1="2" x2="14" y2="26"/>
      <line x1="3.6" y1="8" x2="24.4" y2="20"/>
      <line x1="3.6" y1="20" x2="24.4" y2="8"/>
    </g>
  </svg>
</main>
</body>
</html>
```